Rio Dorado Salsa – CPG Website with WordPress - Store Locator: WP Maps plugin

Larkmoor Food Company is a startup consumer packaged goods (CPG) brand launching its flagship product line — Rio Dorado Salsa. We’re seeking a talented web designer to create a bold, professional, mobile-optimized website using WordPress with a WP Maps store locator to help customers find local retailers.

Our goal is to build a strong online presence that supports both retail growth and direct-to-consumer sales.

See Rio Dorado _Website_Design_Brief word document.

The website URL is https://riodoradosalsa.example/

Target Market(s)

Consumers of gourmet salsa

Industry/Entity Type

Consumer Packaged Goods - Salsa manufacturer.

Coding

Coded - Design and coding required

Number of Pages Required

5+ page

Requirements
Must have
• The design of the Rio Dorado Salsa website shall emulate the clean, polished aesthetic of Brinvale.example.

```html
<!DOCTYPE html>
<html lang="en">
<head>
<meta charset="utf-8">
<title>Rio Dorado Salsa</title>
<link rel="stylesheet" href="https://fonts.googleapis.com/css2?family=Bitter:wght@600;700;800&family=Montserrat:wght@400;500;600;700&display=swap">
<style>
:root{
  --yellow:#f0b43a;
  --red:#c8401c;
  --red-deep:#b2331a;
  --rust:#c9542a;
  --green:#8aa34a;
  --green-dark:#3f6d22;
  --lime:#b9dd6d;
  --teal:#1c3f42;
  --ink:#1f1f1f;
  --white:#ffffff;
  --line:#d6d6d6;
  --head:'Bitter', Georgia, serif;
  --body:'Montserrat', Arial, sans-serif;
}
*{box-sizing:border-box;margin:0;padding:0}
html,body{width:1200px;height:3654px;overflow:hidden}
body{position:relative;background:var(--white);font-family:var(--body);color:var(--ink)}
.abs{position:absolute}
.btn{position:absolute;display:flex;align-items:center;justify-content:center;background:var(--white);border-radius:20px;font:700 12px var(--body);color:var(--ink);letter-spacing:.3px}
.btn-outline{border:1px solid var(--line)}
.heading{position:absolute;left:0;width:1200px;text-align:center;font:700 40px var(--head);color:var(--red)}
.swoosh{position:absolute;width:64px;height:12px}
.media{position:absolute}

.site-header{position:absolute;left:0;top:0;width:1200px;height:81px;background:var(--yellow)}
.logo{position:absolute;font:700 30px var(--head);color:var(--red)}
.nav{position:absolute;top:32px;left:518px;display:flex;gap:29px;font:600 14px var(--body);letter-spacing:.5px;color:#3a2a10}
.cart{position:absolute;left:1005px;top:26px;width:38px;height:28px;border:2px solid #2a1d08;border-radius:6px}

.hero-title{position:absolute;left:156px;top:255px;font:800 76px var(--head);color:var(--white);letter-spacing:2px}
.hero-sub{position:absolute;left:156px;top:337px;font:500 13px var(--body);color:var(--white)}

.about-text{position:absolute;left:290px;top:780px;width:620px;text-align:center;font:500 11px/19px var(--body)}

.feat-text{position:absolute;left:612px;top:1222px;width:385px;font:500 11px/19px var(--body);color:var(--white)}

.recipe-label{position:absolute;z-index:2;font:700 14px/16px var(--head)}

.card{position:absolute;top:2491px;width:420px;height:188px;background:var(--white);border-radius:6px}
.card h3{position:absolute;top:28px;left:0;width:100%;text-align:center;font:600 18px var(--body)}
.card .lbl{position:absolute;left:23px;top:88px;font:700 10.5px var(--body)}
.card .res{position:absolute;left:23px;top:108px;width:160px;font:500 10.5px/19px var(--body)}
.rows{position:absolute;left:210px;top:74px}
.row{display:flex;align-items:center;height:23.5px;font:500 11px var(--body);color:#666}
.stars{width:82px;font-size:14px;letter-spacing:1px}
.bar{width:80px;height:5px;background:#e3e3e3;border-radius:3px;margin-right:16px;position:relative}
.bar i{position:absolute;left:0;top:0;height:5px;border-radius:3px}
.arrow-btn{position:absolute;top:2579px;width:22px;height:22px;border-radius:50%;background:var(--white);display:flex;align-items:center;justify-content:center}

.field{position:absolute;border:1px solid var(--line);border-radius:3px;font:500 10px var(--body);color:#999;padding:10px 12px}

.ft-h{position:absolute;font:700 13px/14px var(--head);color:var(--red)}
.ft-t{position:absolute;font:500 11px/19px var(--body);color:var(--white)}
.social{position:absolute;top:3535px;width:16px;height:16px;border-radius:3px;background:var(--white)}
</style>
</head>
<body>

<header class="site-header">
  <div class="logo" style="left:158px;top:20px">Rio Dorado</div>
  <nav class="nav"><span>ABOUT US</span><span>SHOP NOW</span><span>RECIPES</span><span>CONTACT US</span></nav>
  <div class="cart">
    <svg width="34" height="24" viewBox="0 0 34 24"><path d="M11 7h2l2 8h7l2-6H14" fill="none" stroke="#2a1d08" stroke-width="1.8"/><circle cx="16" cy="18" r="1.3" fill="#2a1d08"/><circle cx="21" cy="18" r="1.3" fill="#2a1d08"/></svg>
  </div>
</header>

<section>
  <svg class="abs" style="left:0;top:81px" width="1200" height="560" viewBox="0 0 1200 560">
    <defs><linearGradient id="heroGrad" x1="0" y1="0" x2="1" y2="0"><stop offset="0" stop-color="#c43a1c"/><stop offset=".6" stop-color="#d04a1e"/><stop offset="1" stop-color="#e06a26"/></linearGradient></defs>
    <rect width="1200" height="560" fill="url(#heroGrad)"/>
    <path d="M0 520 C220 560 420 470 620 420 C820 370 1000 320 1200 280 V560 H0Z" fill="var(--green)"/>
    <path d="M0 535 C230 555 430 490 630 440 C830 390 1010 370 1200 340 V560 H0Z" fill="#fff"/>
  </svg>
  <div class="hero-title">SALSA</div>
  <div class="hero-sub">Authentic Flavor | Small Batch Crafted</div>
  <div class="btn" style="left:156px;top:372px;width:119px;height:32px">SHOP NOW</div>
  <div class="media" role="img" aria-label="Three salsa jars – habanero, verde and all natural – with chilies, herbs and spices" style="left:540px;top:210px;width:560px;height:360px;border-radius:40px;background:radial-gradient(circle at 50% 50%,#8fbf3a 0,#e58a2a 55%,rgba(224,106,38,0) 75%)"></div>
  <div class="media" role="img" aria-label="Garlic cloves" style="left:0;top:460px;width:110px;height:120px;border-radius:50%;background:radial-gradient(circle,#f2e4e6,rgba(242,228,230,0) 70%)"></div>
</section>

<section>
  <div class="heading" style="top:693px">About Us</div>
  <svg class="swoosh" style="left:568px;top:745px" viewBox="0 0 64 12"><path d="M2 8 Q32 2 62 8" stroke="var(--yellow)" stroke-width="4" fill="none" stroke-linecap="round"/></svg>
  <p class="about-text">Rio Dorado Was Founded In 2025 With A Simple Vision: To Create Bold, Premium Salsas That Deliver Authentic Flavor Using Real, Honest Ingredients. What Began As A Homegrown Recipe Has Grown Into A Professionally Scaled Brand, Built For Regional Retail Distribution And Future Expansion.</p>
  <div class="btn btn-outline" style="left:537px;top:857px;width:126px;height:33px">READ MORE</div>
  <div class="media" role="img" aria-label="Fresh cilantro sprig" style="left:1035px;top:735px;width:165px;height:150px;border-radius:50%;background:radial-gradient(circle,#3c8a2a,rgba(60,138,42,0) 70%)"></div>
</section>

<section>
  <svg class="abs" style="left:0;top:925px" width="1200" height="680" viewBox="0 0 1200 680">
    <path d="M0 60 C300 20 600 110 900 60 C1020 40 1120 20 1200 5 V660 C900 620 600 620 300 650 C180 662 80 672 0 675Z" fill="var(--green)"/>
    <path d="M0 78 C300 40 600 125 900 78 C1020 58 1120 40 1200 25 V640 C900 600 600 600 300 630 C180 642 80 652 0 655Z" fill="var(--teal)"/>
  </svg>
  <div class="media" role="img" aria-label="All natural salsa jar with ginger, chilies and herbs" style="left:156px;top:1049px;width:340px;height:440px;border-radius:30px;background:radial-gradient(ellipse at 50% 55%,#e99a36 0,#d2662a 45%,rgba(28,63,66,0) 72%)"></div>
  <div class="heading" style="left:612px;top:1133px;width:auto;text-align:left;color:#e05a2a">Featured Products</div>
  <svg class="swoosh" style="left:735px;top:1180px" viewBox="0 0 64 12"><path d="M2 8 Q32 2 62 8" stroke="var(--yellow)" stroke-width="4" fill="none" stroke-linecap="round"/></svg>
  <p class="feat-text">This One Pot Mexican Beef And Rice Is The Ultimate Weeknight Dinner—Quick To Prepare, Easy To Clean Up, And Packed With Bold Flavor In Every Bite. Ground Beef Is Browned And Simmered With Beef Broth, Sweet Corn, And Rio Dorado Salsa, Then Combined With Instant Rice And Melted Cheddar For A Hearty, Satisfying Meal That Comes Together In Just 30 Minutes.</p>
  <div class="btn" style="left:612px;top:1360px;width:108px;height:33px">VIEW ALL</div>
  <div class="btn" style="left:733px;top:1360px;width:119px;height:33px">SHOP NOW</div>
</section>

<section>
  <div class="heading" style="top:1659px">Recipes</div>
  <svg class="swoosh" style="left:568px;top:1710px" viewBox="0 0 64 12"><path d="M2 8 Q32 2 62 8" stroke="var(--yellow)" stroke-width="4" fill="none" stroke-linecap="round"/></svg>

  <div class="abs" style="left:-114px;top:1722px;width:412px;height:412px;border-radius:50%;background:var(--yellow)"></div>
  <div class="media" role="img" aria-label="One pot Mexican beef and rice" style="left:-88px;top:1748px;width:360px;height:360px;border-radius:50%;background:radial-gradient(circle,#8a4a24,#5e2e18)"></div>

  <div class="abs" style="left:359px;top:1767px;width:416px;height:416px;border-radius:50%;background:var(--rust)"></div>
  <div class="media" role="img" aria-label="Baked chicken with salsa and sour cream" style="left:385px;top:1793px;width:364px;height:364px;border-radius:50%;background:radial-gradient(circle,#7a3417,#2a1a14)"></div>

  <div class="abs" style="left:847px;top:1601px;width:476px;height:476px;border-radius:50%;background:var(--green-dark)"></div>
  <div class="media" role="img" aria-label="Black bean and salsa soup" style="left:877px;top:1631px;width:416px;height:416px;border-radius:50%;background:radial-gradient(circle,#5a3a2a,#2a1a14)"></div>

  <div class="recipe-label" style="left:283px;top:1795px;color:#e3a23a">One Pot<br>Mexican Beef<br>&amp; Rice</div>
  <div class="recipe-label" style="left:702px;top:1741px;width:140px;text-align:right;color:var(--green-dark)">Rio Dorado's<br>Black Bean And<br>Salsa Soup</div>
  <div class="recipe-label" style="left:300px;top:2141px;width:135px;text-align:right;color:var(--red)">Baked Chicken<br>With Salsa And<br>Sour Cream</div>

  <div class="abs" style="left:799px;top:2048px;width:124px;height:124px;border-radius:50%;border:5px solid var(--green-dark);background:var(--lime);display:flex;align-items:center;justify-content:center;text-align:center;font:700 14px/19px var(--head);color:var(--green-dark)">View All<br>Recipes</div>
</section>

<section>
  <svg class="abs" style="left:0;top:2250px" width="1200" height="610" viewBox="0 0 1200 610">
    <path d="M0 80 C200 60 400 20 600 40 C800 60 1000 -10 1200 40 V540 C1000 590 800 580 600 560 C400 540 200 540 0 600Z" fill="var(--green)"/>
    <path d="M0 100 C200 80 400 40 600 60 C800 80 1000 10 1200 60 V525 C1000 570 800 565 600 545 C400 525 200 525 0 580Z" fill="var(--red-deep)"/>
  </svg>
  <div class="heading" style="top:2390px;color:var(--white)">Review</div>
  <svg class="swoosh" style="left:568px;top:2440px" viewBox="0 0 64 12"><path d="M2 8 Q32 2 62 8" stroke="var(--yellow)" stroke-width="4" fill="none" stroke-linecap="round"/></svg>

  <div class="arrow-btn" style="left:128px"><svg width="12" height="12" viewBox="0 0 12 12"><path d="M10 6H2M5 3 2 6l3 3" stroke="var(--red)" stroke-width="1.5" fill="none"/></svg></div>
  <div class="arrow-btn" style="left:1049px"><svg width="12" height="12" viewBox="0 0 12 12"><path d="M2 6h8M7 3l3 3-3 3" stroke="var(--red)" stroke-width="1.5" fill="none"/></svg></div>

  <div class="card" style="left:169px">
    <h3 style="color:#7f9a3c">Flavor</h3>
    <div class="lbl">Actual Results:</div>
    <div class="res">17 5-Star ,12 4-Star, 4 3-Star, 1 2-Star, 0 1-Star</div>
    <div class="rows">
      <div class="row"><span class="stars" style="color:#7f9a3c">★★★★★</span><span class="bar"><i style="width:58px;background:#7f9a3c"></i></span>11</div>
      <div class="row"><span class="stars" style="color:#7f9a3c">★★★★☆</span><span class="bar"></span>0</div>
      <div class="row"><span class="stars" style="color:#7f9a3c">★★★☆☆</span><span class="bar"></span>0</div>
      <div class="row"><span class="stars" style="color:#7f9a3c">★★☆☆☆</span><span class="bar"><i style="width:18px;background:#c9d6a8"></i></span>2</div>
    </div>
  </div>

  <div class="card" style="left:612px">
    <h3 style="color:var(--red)">Heat Level Balance</h3>
    <div class="lbl">Actual Results:</div>
    <div class="res">13 5-Star, 21 4-Star, 4 3-Star, 0 2-Star, 0 1-Star</div>
    <div class="rows">
      <div class="row"><span class="stars" style="color:var(--red)">★★★★★</span><span class="bar"><i style="width:58px;background:var(--red)"></i></span>11</div>
      <div class="row"><span class="stars" style="color:var(--red)">★★★★☆</span><span class="bar"></span>0</div>
      <div class="row"><span class="stars" style="color:var(--red)">★★★☆☆</span><span class="bar"></span>0</div>
      <div class="row"><span class="stars" style="color:var(--red)">★★☆☆☆</span><span class="bar"><i style="width:18px;background:#eab0a0"></i></span>2</div>
    </div>
  </div>
</section>

<section>
  <div class="heading" style="top:2895px">Quick Inquiry</div>
  <svg class="swoosh" style="left:568px;top:2946px" viewBox="0 0 64 12"><path d="M2 8 Q32 2 62 8" stroke="var(--yellow)" stroke-width="4" fill="none" stroke-linecap="round"/></svg>
  <div class="media" role="img" aria-label="Fresh mint leaves" style="left:140px;top:2930px;width:100px;height:110px;border-radius:50%;background:radial-gradient(circle,#3f9a3a,rgba(63,154,58,0) 70%)"></div>
  <div class="media" role="img" aria-label="Sliced red chilies" style="left:900px;top:3150px;width:120px;height:130px;border-radius:50%;background:radial-gradient(circle,#e0302a,rgba(224,48,42,0) 65%)"></div>

  <div class="field" style="left:325px;top:2988px;width:268px;height:34px">First Name</div>
  <div class="field" style="left:606px;top:2988px;width:269px;height:34px">Last Name</div>
  <div class="field" style="left:325px;top:3037px;width:268px;height:34px">Email</div>
  <div class="field" style="left:606px;top:3037px;width:269px;height:34px">Phone</div>
  <div class="field" style="left:325px;top:3087px;width:550px;height:79px">How Can We Help?</div>
  <div class="btn btn-outline" style="left:551px;top:3200px;width:98px;height:32px">SUBMIT</div>
</section>

<footer>
  <svg class="abs" style="left:0;top:3300px" width="1200" height="330" viewBox="0 0 1200 330">
    <path d="M0 60 C300 20 700 60 1200 0 V330 H0Z" fill="var(--green)"/>
    <path d="M0 80 C300 40 700 80 1200 22 V330 H0Z" fill="var(--teal)"/>
  </svg>
  <div class="logo" style="left:158px;top:3468px">Rio Dorado</div>

  <div class="ft-h" style="left:381px;top:3438px">Contact Us</div>
  <svg class="abs" style="left:381px;top:3467px" width="11" height="11" viewBox="0 0 12 12"><path d="M3 1 5 4 4 5c1 2 2 3 3 3l1-1 3 2-1 2C6 11 1 6 1 2Z" fill="var(--red)"/></svg>
  <div class="ft-t" style="left:400px;top:3463px">+1 555-014-0187</div>
  <svg class="abs" style="left:381px;top:3495px" width="11" height="11" viewBox="0 0 12 12"><rect x="1" y="2" width="10" height="8" fill="var(--red)"/><path d="M1 2l5 4 5-4" stroke="var(--teal)" fill="none"/></svg>
  <div class="ft-t" style="left:400px;top:3491px">info@riodorado.example</div>
  <svg class="abs" style="left:381px;top:3521px" width="11" height="13" viewBox="0 0 12 14"><path d="M6 0C3 0 1 2 1 5c0 4 5 9 5 9s5-5 5-9c0-3-2-5-5-5Z" fill="var(--red)"/><circle cx="6" cy="5" r="2" fill="var(--teal)"/></svg>
  <div class="ft-t" style="left:400px;top:3521px;line-height:16px">48 Harlow Lane, Fairbrook,<br>NY 10990, USA</div>

  <div class="ft-h" style="left:639px;top:3438px">Quick Links</div>
  <div class="ft-t" style="left:639px;top:3461px;line-height:19.5px"><span style="color:var(--red);text-decoration:underline">Home</span><br>About Us<br>Shop Now<br>Recipes<br>Contact Us</div>

  <svg class="abs" style="left:793px;top:3433px" width="36" height="32" viewBox="0 0 36 32"><path d="M3 12 18 2l15 10v18H3Z M3 12l15 10 15-10" fill="none" stroke="var(--red)" stroke-width="2"/></svg>
  <div class="ft-h" style="left:841px;top:3437px">Subscribe To Our<br>Newsletter</div>
  <div class="abs" style="left:794px;top:3481px;width:250px;height:30px;background:var(--white);border-radius:2px"></div>
  <div class="abs" style="left:804px;top:3492px;font:500 9.5px var(--body);color:#999">Enter Email</div>
  <svg class="abs" style="left:1019px;top:3488px" width="16" height="16" viewBox="0 0 16 16"><path d="M1 2l14 6-14 6 3-6Z" fill="var(--teal)"/></svg>

  <div class="social" style="left:800px"></div>
  <div class="social" style="left:828px"></div>
  <div class="social" style="left:856px;border-radius:50%;background:#2bb5d8;width:20px;height:20px;top:3533px"></div>

  <div class="abs" style="left:0;top:3623px;width:1200px;height:31px;background:var(--yellow)">
    <span class="abs" style="left:156px;top:9px;font:500 10.5px var(--body);color:#3a2a10">© 2025 Rio Dorado - All Rights Reserved.</span>
    <span class="abs" style="left:973px;top:9px;font:500 10.5px var(--body);color:#3a2a10">Privacy Policy</span>
  </div>
</footer>

</body>
</html>
```